Diagram, Brochure and Flyer Design

Veltrion Systems is a cyber security software company that develops, implements and supports cyber security and information management end-point solutions that solve critical security and compliance issues when organisations transmit private or business sensitive information.

We do this by interfacing directly with an organisation’s existing information management systems and line of business applications to provide a ‘bridge’ to essential security systems and platforms for data that is transmitted via email, FTP, ‘Bring Your Own Devices’ (‘BYOD’) such as smart phones, iPads, etc, or during collaboration with third party organisations that use different systems and applications, and the Cloud.

Veltrion Systems, flagship product "Lumora" enables simple deployment by organisations with minimal change management to secure an organisation’s vulnerable digital assets.

Most importantly, Lumora enables organisations to secure data without replacing or losing functionality from existing systems (i.e. for compliance, collaboration or audit purposes, etc.).

We are seeking to design a series of corporate brochures, diagrams and flyers for an information security company as described above.

www.veltrion.com.au

Target Market(s)

Government and Corporates

Font styles to use
Sans Serif

Requirements
Must have
• Clean and professional
Nice to have
• Consistent look and feel
Should not have
• Too much wording (text)

```html
<!DOCTYPE html>
<html lang="en">
<head>
<meta charset="utf-8">
<title>Lumora Functionality Set – Flyer Front and Back</title>
<link href="https://fonts.googleapis.com/css2?family=Arimo:wght@400&family=Roboto+Condensed:wght@400;700&family=Open+Sans:wght@400;600;700&display=swap" rel="stylesheet">
<style>
  :root {
    --orange: #e36c0d;
    --ink: #3d3d3d;
    --ink-dark: #1e1e1e;
    --rule: #c9c9c9;
    --paper: #ffffff;
    --backdrop: #ececec;
    --photo-slate: #4d5a63;
    --photo-steel: #9fb1c8;
    --photo-skin: #d8c2b3;
  }
  * { margin: 0; padding: 0; box-sizing: border-box; }
  html, body { width: 1200px; height: 1200px; overflow: hidden; background: var(--backdrop); }
  .stage {
    position: absolute; left: 0; top: 0;
    width: 1400px; height: 1400px;
    transform: scale(0.857143); transform-origin: 0 0;
  }
  .card {
    position: absolute; top: 478px;
    width: 603px; height: 429px;
    background: var(--paper);
    overflow: hidden;
    box-shadow: 0 2px 6px rgba(0,0,0,0.12);
  }
  .card--front { left: 44px; }
  .card--back { left: 733px; }
  .card svg.shapes { position: absolute; left: 0; top: 0; }

  .product-title {
    position: absolute; left: 40px; top: 26px;
    font-family: 'Arimo', Arial, sans-serif; font-weight: 400;
    font-size: 80px; line-height: 1; color: var(--orange); letter-spacing: 1px;
  }
  .product-subtitle {
    position: absolute; left: 42px; top: 100px;
    font-family: 'Roboto Condensed', 'Arial Narrow', sans-serif; font-weight: 700;
    font-size: 41px; line-height: 1; color: var(--ink); letter-spacing: 0.5px;
  }
  .tagline {
    position: absolute; left: 42px; top: 171px;
    font-family: 'Roboto Condensed', 'Arial Narrow', sans-serif; font-weight: 400;
    font-size: 22px; line-height: 1; color: var(--paper);
  }
  .front-url {
    position: absolute; left: 43px; top: 376px;
    font-family: 'Open Sans', Arial, sans-serif; font-weight: 600;
    font-size: 14px; letter-spacing: 1.6px; color: var(--ink-dark);
  }
  .brand {
    position: absolute;
    display: flex; flex-direction: column; align-items: center; gap: 8px;
    font-family: 'Open Sans', Arial, sans-serif; font-weight: 700;
    font-size: 14px; line-height: 1.05; color: var(--ink-dark); text-align: center;
  }
  .brand__mark { width: 26px; height: 26px; background: var(--ink-dark); }
  .card--front .brand { left: 486px; top: 50px; width: 110px; }
  .card--back .brand { left: 330px; top: 56px; width: 110px; }

  .contact-heading {
    position: absolute; left: 227px; right: 0; top: 194px;
    text-align: center; padding-right: 62px;
    font-family: 'Open Sans', Arial, sans-serif; font-weight: 600;
    font-size: 19px; color: var(--orange);
  }
  .contact-item {
    position: absolute; display: flex; gap: 6px; align-items: flex-start;
    font-family: 'Open Sans', Arial, sans-serif; font-weight: 600;
    font-size: 9.5px; line-height: 1.35; color: var(--ink);
  }
  .contact-item svg { flex: none; margin-top: 1px; }
  .contact-item--address { left: 248px; top: 253px; }
  .contact-item--lines { left: 412px; top: 253px; }
  .url-button {
    position: absolute; left: 275px; top: 302px; width: 207px; height: 26px;
    background: var(--orange); color: var(--paper);
    font-family: 'Open Sans', Arial, sans-serif; font-weight: 600;
    font-size: 14px; letter-spacing: 1.4px;
    display: flex; align-items: center; justify-content: center;
  }
</style>
</head>
<body>
<main class="stage">

  <section class="card card--front">
    <svg class="shapes" width="603" height="429" viewBox="0 0 603 429">
      <defs>
        <linearGradient id="cloud-photo" x1="0" y1="0" x2="1" y2="0">
          <stop offset="0" stop-color="#2e3844"/>
          <stop offset="0.45" stop-color="#6e7b80"/>
          <stop offset="1" stop-color="#b9c2c4"/>
        </linearGradient>
        <linearGradient id="security-photo" x1="0" y1="1" x2="1" y2="0">
          <stop offset="0" stop-color="#e9eef5"/>
          <stop offset="0.5" stop-color="#b7c6da"/>
          <stop offset="1" stop-color="#7f92ab"/>
        </linearGradient>
      </defs>
      <polygon points="356,0 603,0 603,242" fill="#f4f4f4"/>
      <line x1="356" y1="0" x2="603" y2="247" stroke="#d9d9d9" stroke-width="1.5"/>
      <polygon points="0,167 468,167 438,200 0,200" fill="var(--orange)"/>
      <polygon points="0,214 426,214 296,357 0,357" fill="url(#cloud-photo)" role="img" aria-label="Businessman touching a cloud icon linked to devices, email and globe icons"/>
      <line x1="496" y1="147" x2="206" y2="429" stroke="#d9d9d9" stroke-width="1.5"/>
      <polygon points="272,429 502,202 603,300 603,429" fill="url(#security-photo)" role="img" aria-label="Open hand presenting a glowing shield with a padlock"/>
      <line x1="272" y1="429" x2="502" y2="202" stroke="#ffffff" stroke-width="6"/>
    </svg>
    <h1 class="product-title">LUMORA</h1>
    <h2 class="product-subtitle">FUNCTIONALITY SET</h2>
    <p class="tagline">Next Generation Data Sharing Platform</p>
    <div class="brand"><span class="brand__mark"></span><span>Veltrion<br>Systems</span></div>
    <p class="front-url">www.veltrion.com.au</p>
  </section>

  <section class="card card--back">
    <svg class="shapes" width="603" height="429" viewBox="0 0 603 429">
      <defs>
        <linearGradient id="agent-photo" x1="0" y1="0" x2="1" y2="1">
          <stop offset="0" stop-color="#f2f2f2"/>
          <stop offset="0.5" stop-color="var(--photo-skin)"/>
          <stop offset="1" stop-color="#eeeeee"/>
        </linearGradient>
      </defs>
      <line x1="227" y1="185" x2="603" y2="185" stroke="var(--rule)" stroke-width="1.5"/>
      <line x1="227" y1="230" x2="603" y2="230" stroke="var(--rule)" stroke-width="1.5"/>
      <polygon points="0,0 52,0 242,207 52,429 0,429 0,418 190,207 0,18" fill="var(--orange)"/>
      <polygon points="112,97 222,207 112,317 2,207" fill="url(#agent-photo)" stroke="var(--orange)" stroke-width="4" role="img" aria-label="Customer support agent wearing a headset with colleagues behind"/>
      <polygon points="0,186 22,207 0,228" fill="none" stroke="var(--orange)" stroke-width="4"/>
    </svg>
    <div class="brand"><span class="brand__mark"></span><span>Veltrion<br>Systems</span></div>
    <h2 class="contact-heading">Contact Us</h2>
    <div class="contact-item contact-item--address">
      <svg width="9" height="12" viewBox="0 0 9 12"><path d="M4.5 0C2 0 0 2 0 4.4 0 7.5 4.5 12 4.5 12S9 7.5 9 4.4C9 2 7 0 4.5 0z" fill="var(--orange)"/><circle cx="4.5" cy="4.4" r="1.7" fill="#fff"/></svg>
      <span>12 Harlow Street Melbourne,<br>Blackburn 3130 Australia</span>
    </div>
    <div class="contact-item contact-item--lines">
      <svg width="9" height="22" viewBox="0 0 9 22"><path d="M1.5 0.5l2 0 1 2.5-1.3 1a5 5 0 0 0 2.8 2.8l1-1.3 2.5 1v2C8.5 9 1 8 0.5 1.5z" fill="var(--orange)"/><rect x="0.5" y="14" width="8" height="6" rx="1" fill="none" stroke="var(--orange)" stroke-width="1.2"/><path d="M0.8 14.5l3.7 3 3.7-3" fill="none" stroke="var(--orange)" stroke-width="1.1"/></svg>
      <span>61 400 123 456<br>info@veltrion.com.au</span>
    </div>
    <div class="url-button">www.veltrion.com.au</div>
  </section>

</main>
</body>
</html>
```